Sports Therapy and Personal Training

I need a business card design for a new business based in Toronto called "Holbrin Athletics" I am a sports therapist as well as a strength and conditioning coach, therefore I work mainly with high level athletes and physically active people. I am starting my own therapy/training business. The services I will be offering include fitness consultation, personal training, athlete assessments, and rehabilitation therapy. These services will be delivered in peoples homes and/or a facility in which I rent space.

The final design should communicate "high-end" and "quality"

Target Market(s)

athletes and physically active people

Industry/Entity Type

Fitness

Requirements
Must have
• 1. The business logo - files attached

2. my name and credentials

Derek Falloway - CAT(C), CK, CSCS,

Certified Athletic Therapist
Strength and Conditioning Specialist

3. website - www.holbrinathletics.example

4. email address - derek@holbrinathletics.example

5. phone number

```html
<!DOCTYPE html>
<html lang="en">
<head>
<meta charset="utf-8">
<title>Holbrin Athletics – Business Cards</title>
<link rel="stylesheet" href="https://fonts.googleapis.com/css2?family=Open+Sans:wght@400;600&family=Arimo:wght@400&display=swap">
<style>
  :root {
    --backdrop: #d9d9d9;
    --card-white: #ffffff;
    --ink: #1c1c1c;
    --accent-red: #d7261e;
    --red-deep: #8e1a16;
    --red-mid: #a9201a;
    --red-glow: #d9241c;
    --on-red: #ffffff;
    --on-red-soft: #f3dcda;
    --watermark: #e6e6e6;
  }
  * { margin: 0; padding: 0; box-sizing: border-box; }
  html, body { width: 1200px; height: 951px; overflow: hidden; }
  body {
    background: var(--backdrop);
    position: relative;
    font-family: "Open Sans", Verdana, sans-serif;
  }
  .card {
    position: absolute;
    width: 560px;
    height: 320px;
    box-shadow: 0 6px 18px rgba(0,0,0,0.25);
  }

  /* Front: locations card */
  .card--locations {
    left: 70px; top: 80px;
    background: var(--card-white);
    font-family: "Arimo", Arial, sans-serif;
    color: var(--ink);
  }
  .locations__mark {
    position: absolute;
    left: 0; right: 0; top: 78px;
    text-align: center;
    font-family: "Open Sans", Verdana, sans-serif;
    font-weight: 600;
    font-size: 46px;
    color: var(--watermark);
  }
  .locations__heading {
    position: absolute;
    left: 0; right: 0; top: 218px;
    text-align: center;
    font-size: 15px;
    letter-spacing: 0.3px;
  }
  .locations__heading .accent { color: var(--accent-red); }
  .locations__list {
    position: absolute;
    left: 20px; right: 20px; top: 242px;
    list-style: none;
    font-size: 12.5px;
    line-height: 20px;
    text-align: center;
  }
  .locations__venue { color: var(--accent-red); }

  /* Back: contact card */
  .card--contact {
    left: 560px; top: 470px;
    background: radial-gradient(ellipse at 62% 45%, var(--red-glow) 0%, var(--red-mid) 45%, var(--red-deep) 100%);
    color: var(--on-red);
  }
  .brand {
    position: absolute;
    left: 30px; top: 30px;
    display: flex; align-items: center; gap: 14px;
  }
  .brand__square {
    width: 44px; height: 44px;
    background: var(--on-red);
  }
  .brand__name {
    font-weight: 600;
    font-size: 30px;
    letter-spacing: 0.5px;
  }
  .brand__tagline {
    position: absolute;
    left: 88px; top: 80px;
    font-size: 10.5px;
    letter-spacing: 1.8px;
    text-transform: uppercase;
    color: var(--on-red-soft);
  }
  .person { position: absolute; left: 30px; top: 122px; }
  .person__name { font-size: 20px; line-height: 24px; }
  .person__credentials { font-size: 13px; line-height: 18px; }
  .person__roles { margin-top: 14px; font-size: 14px; line-height: 18px; }
  .contact-list {
    list-style: none;
    margin-top: 12px;
    font-size: 14px;
    line-height: 20px;
  }
</style>
</head>
<body>
  <section class="card card--locations" aria-label="Training locations">
    <div class="locations__mark">Holbrin Athletics</div>
    <p class="locations__heading">WORKING <span class="accent">OUT OF</span></p>
    <ul class="locations__list">
      <li><span class="locations__venue">Northfield Training Hall,</span> 418 Crestline Road, Unit 5, Ashbury, Ontario, L0A 2B3</li>
      <li><span class="locations__venue">Summit Athletes Training Centre,</span> 72 Larkspur Avenue, Elmvale, Ontario, L0B 4C7</li>
    </ul>
  </section>

  <section class="card card--contact" aria-label="Contact details">
    <div class="brand">
      <span class="brand__square"></span>
      <span class="brand__name">Holbrin Athletics</span>
    </div>
    <p class="brand__tagline">Sports Medicine • Strength and Conditioning</p>
    <div class="person">
      <p class="person__name">Derek Falloway</p>
      <p class="person__credentials">CAT(C), CK, CSCS</p>
      <p class="person__roles">Certified Athletic Therapist<br>Strength and Conditioning Specialist</p>
      <ul class="contact-list">
        <li>P: 555-014-0192</li>
        <li>W: www.holbrinathletics.example</li>
        <li>E: derek@holbrinathletics.example</li>
      </ul>
    </div>
  </section>
</body>
</html>
```